Business Card for Managing Partner Investment Fund

To create a business card template for an investment fund manager. Business card should be more professional in nature, not too colorful, more upscale, and created using the attached logos and fund name files. I would prefer a black or gray color scheme, but am open to the use of color as well. I would prefer a double sided business card, but open to single sided business card designs as well. The business card should include: name, title, and contact information, as well as logo and company name. I would prefer a more stream-lined, simple business card design.
Updates
Address: 4190 NE 38th Ter. Ocala, FL 34470
Email: talvin47@quorimail.net
Phone: 561-347-9162
Title: managing partner
Name: Dorian Velsky
Fund Name: Ambergate Capital
Logos can be found in files attached to the brief
Target Market(s)
potential investors, other fund managers
Industry/Entity Type
Finance
Contact Information for Business Card
Name on card: Dorian Velsky
Title: Managing Partner
Colors
Designer to choose colors to be used in the design.
Requirements
Must have
- Phone number
- email address
- physical address
- title
- name
- logo
- Fund name
Nice to have
- simple layout
Should not have
- too many colors, busy fonts,

```html
<!DOCTYPE html>
<html lang="en">
<head>
<meta charset="utf-8">
<title>Ambergate Capital – Business Card</title>
<link href="https://fonts.googleapis.com/css2?family=Open+Sans:wght@400;600;700&display=swap" rel="stylesheet">
<style>
  :root{
    --backdrop:#3b3330;
    --card:#151515;
    --card-edge:#1e1e1e;
    --mark:#6c6c6c;
    --name:#8a8a8a;
    --text:#d6d6d6;
    --muted:#9a9a9a;
    --rule:#7a7a7a;
  }
  *{box-sizing:border-box;margin:0;padding:0}
  html,body{width:1200px;height:864px;overflow:hidden}
  body{
    background:var(--backdrop);
    font-family:"Open Sans",Arial,sans-serif;
    position:relative;
  }
  .card{
    position:absolute;
    width:520px;height:298px;
    background:var(--card);
    border:1px solid var(--card-edge);
    box-shadow:0 14px 30px rgba(0,0,0,.45);
  }
  .card--front{left:70px;top:110px}
  .card--back{left:610px;top:420px}

  .wordmark{
    display:flex;align-items:center;gap:10px;
    color:var(--mark);
    font-weight:700;
    letter-spacing:.08em;
    text-transform:uppercase;
  }
  .wordmark__square{
    width:14px;height:14px;background:var(--mark);flex:none;
  }

  .card--front .wordmark{
    position:absolute;left:0;right:0;top:112px;
    justify-content:center;font-size:26px;
  }
  .front__web{
    position:absolute;left:0;right:0;top:178px;
    text-align:center;
    color:var(--muted);
    font-size:13px;letter-spacing:.32em;
  }

  .card--back .wordmark{
    position:absolute;left:26px;top:128px;
    font-size:19px;gap:8px;
  }
  .card--back .wordmark__square{width:11px;height:11px}
  .back__divider{
    position:absolute;left:282px;top:54px;
    width:2px;height:190px;
    background:linear-gradient(to bottom,transparent,var(--rule) 50%,transparent);
  }
  .contact{
    position:absolute;left:304px;top:70px;
    color:var(--text);
    font-size:13px;line-height:1.45;
  }
  .contact__name{
    color:var(--name);font-weight:700;font-size:16px;
    text-transform:uppercase;letter-spacing:.02em;line-height:1.2;
  }
  .contact__title{
    color:var(--name);font-size:15px;text-transform:uppercase;
    margin-bottom:10px;line-height:1.2;
  }
  .contact__address{margin-bottom:6px}
  .contact__row{display:flex;align-items:center;gap:8px}
  .contact__icon{width:11px;height:11px;flex:none;fill:var(--muted)}
</style>
</head>
<body>
  <section class="card card--front" aria-label="Card front">
    <div class="wordmark"><span class="wordmark__square"></span>Ambergate Capital</div>
    <p class="front__web">www.ambergatefund.net</p>
  </section>

  <section class="card card--back" aria-label="Card back">
    <div class="wordmark"><span class="wordmark__square"></span>Ambergate Capital</div>
    <div class="back__divider"></div>
    <div class="contact">
      <p class="contact__name">Dorian Velsky</p>
      <p class="contact__title">Managing Partner</p>
      <p class="contact__address">4190 NE 38th Ter.<br>Ocala, FL 34470</p>
      <p class="contact__row">
        <svg class="contact__icon" viewBox="0 0 12 12" aria-hidden="true"><path d="M2.5 1l2 2-1 1.3a7 7 0 0 0 4.2 4.2L9 7.5l2 2-1.4 1.5C5.4 11 1 6.6 1 2.4z"/></svg>
        561-347-9162
      </p>
      <p class="contact__row">
        <svg class="contact__icon" viewBox="0 0 12 12" aria-hidden="true"><path d="M1 2.5h10v7H1z M1.6 3l4.4 3.3L10.4 3" fill="none" stroke="#9a9a9a" stroke-width="1.2"/></svg>
        talvin47@quorimail.net
      </p>
      <p class="contact__row">
        <svg class="contact__icon" viewBox="0 0 12 12" aria-hidden="true"><circle cx="6" cy="6" r="5" fill="none" stroke="#9a9a9a" stroke-width="1.2"/><path d="M1 6h10M6 1c2 2.5 2 7.5 0 10M6 1c-2 2.5-2 7.5 0 10" fill="none" stroke="#9a9a9a" stroke-width="1"/></svg>
        www.ambergatefund.net
      </p>
    </div>
  </section>
</body>
</html>
```